brownie sticker

i need a sticker to wrap around a clear rectangle box that will contain chocolate brownies. the sticker must be 17cm x 7 cm.
the sticker will be placed in the folowing direction.
7cm of the sticker on front of box, 3cm for each side of the box, and 4 cm on the bottom to seal the box closed.
I HAVE ATTACHED A VERY ROUGH PICTURE FOR YOU TO SEE POSITION AND DIRECTION OF STICKER.

Target Market(s)

our product will be mainly seen in upmarket grocery stores and farmers markets.

Requirements
Must have
• IT MUST CONTAIN THE FOLLOWING IN SMALL PRINT at the bottom of the sticker...
produced by marisols bakehouse
48 fenwick st
cheltenham
vic 3192
ph: 047396581
email: marisolsbakehouse@quillmail.example

```html
<!DOCTYPE html>
<html lang="en">
<head>
<meta charset="utf-8">
<title>Marisol's Bakehouse – Box Sticker General View</title>
<link rel="stylesheet" href="https://fonts.googleapis.com/css2?family=Cinzel:wght@400&family=Open+Sans:wght@400;700&family=Questrial&display=swap">
<style>
  :root {
    --page-bg: #f6f5ef;
    --page-edge: #ecebe3;
    --sticker-kraft: #d3c6b0;
    --choc-brown: #5b2711;
    --label-ink: #2f2f2f;
    --tick-grey: #8a8a86;
  }
  * { margin: 0; padding: 0; box-sizing: border-box; }
  html, body { width: 1200px; height: 1000px; overflow: hidden; }
  body {
    position: relative;
    background: radial-gradient(ellipse at 50% 45%, var(--page-bg) 55%, var(--page-edge) 100%);
    font-family: "Open Sans", Arial, sans-serif;
    color: var(--label-ink);
  }

  /* dimension column */
  .dimension-tick {
    position: absolute; left: 318px; width: 62px; height: 1px;
    background: var(--tick-grey);
  }
  .dimension-value {
    position: absolute; right: 905px; font-size: 31px; line-height: 1;
    transform: translateY(-50%);
  }
  .panel-name {
    position: absolute; left: 785px; font-size: 32px; line-height: 1;
    letter-spacing: 1px; transform: translateY(-50%);
  }

  /* the sticker strip */
  .sticker {
    position: absolute; left: 381px; top: 30px; width: 377px; height: 917px;
    background: var(--sticker-kraft);
  }
  .sticker-rule {
    position: absolute; top: 0; bottom: 0; width: 2px; background: var(--choc-brown);
  }
  .sticker-rule.left { left: 11px; }
  .sticker-rule.right { right: 11px; }

  .producer-details {
    position: absolute; left: 0; right: 0; top: 238px;
    transform: rotate(180deg);
    text-align: center; color: var(--choc-brown);
    font-family: "Questrial", "Century Gothic", Arial, sans-serif;
    font-size: 15.5px; line-height: 1;
  }
  .producer-details p { height: 21px; }
  .producer-details p.gap { height: 25px; }

  .brand-lockup {
    position: absolute; left: 0; right: 0; top: 488px;
    text-align: center; color: var(--choc-brown);
    font-family: "Cinzel", Georgia, serif; font-weight: 400;
  }
  .brand-dot {
    display: block; margin: 0 auto 40px; width: 46px; height: 46px;
  }
  .brand-name { font-size: 44px; line-height: 1; letter-spacing: 2px; }
  .brand-sub { margin-top: 8px; font-size: 19px; line-height: 1; letter-spacing: 7px; padding-left: 7px; }

  .view-title {
    position: absolute; left: 835px; top: 922px;
    font-size: 43px; font-weight: 700; line-height: 1; color: #363636;
  }
</style>
</head>
<body>
  <div class="dimension-tick" style="top:30px"></div>
  <div class="dimension-tick" style="top:245px"></div>
  <div class="dimension-tick" style="top:407px"></div>
  <div class="dimension-tick" style="top:785px"></div>
  <div class="dimension-tick" style="top:947px"></div>

  <div class="dimension-value" style="top:147px">4 cm</div>
  <div class="dimension-value" style="top:333px">3 cm</div>
  <div class="dimension-value" style="top:577px">7 cm</div>
  <div class="dimension-value" style="top:866px">3 cm</div>

  <div class="panel-name" style="top:146px">BOTTOM</div>
  <div class="panel-name" style="top:332px">BACK</div>
  <div class="panel-name" style="top:576px">TOP</div>
  <div class="panel-name" style="top:865px">FRONT</div>

  <div class="sticker">
    <div class="sticker-rule left"></div>
    <div class="sticker-rule right"></div>

    <div class="producer-details">
      <p>produced by MARISOL'S BAKEHOUSE</p>
      <p>48 Fenwick St</p>
      <p class="gap">Brindlewood VIC 3988</p>
      <p>phone : 047 396 581</p>
      <p>email : marisolsbakehouse@quillmail.example</p>
    </div>

    <div class="brand-lockup">
      <svg class="brand-dot" viewBox="0 0 46 46" aria-hidden="true">
        <circle cx="23" cy="23" r="23" fill="#5b2711"/>
      </svg>
      <div class="brand-name">MARISOL'S</div>
      <div class="brand-sub">BAKEHOUSE</div>
    </div>
  </div>

  <div class="view-title">GENERAL VIEW</div>
</body>
</html>
```